Trade Show Marlow 3x3 booth schel scheme

We would like to have full coverage design for 3x3 booth scheel

2x2 pop up Counter (1200mm wide x 900mm high x 400mm deep)
Our company provides food safety training, consultancy and food safety app service for hospitality businesses.

```html
<!DOCTYPE html>
<html lang="en">
<head>
<meta charset="utf-8">
<title>Verdano – Trade Show Booth Scheme</title>
<link rel="stylesheet" href="https://fonts.googleapis.com/css2?family=Poppins:wght@400;500;600;700&family=Open+Sans:wght@700&display=swap">
<style>
  :root {
    --stage: #e0dcdd;
    --lime: #d4d600;
    --ink: #1a1a1a;
    --white: #ffffff;
    --mist: #ececec;
    --body-grey: #3a3a3a;
  }
  * { margin: 0; padding: 0; box-sizing: border-box; }
  html, body { width: 1200px; height: 972px; overflow: hidden; }
  body {
    background: var(--stage);
    font-family: "Poppins", sans-serif;
    position: relative;
  }

  /* ---------- 3x3 back wall ---------- */
  .back-wall {
    position: absolute;
    left: 124px; top: 190px;
    width: 592px; height: 592px;
    overflow: hidden;
    box-shadow: 0 4px 6px rgba(0,0,0,0.25);
  }
  .back-wall .wall-shapes { position: absolute; inset: 0; }
  .wall-phone {
    position: absolute; left: 46px; top: 26px;
    font-weight: 600; font-size: 22px; color: var(--ink);
    letter-spacing: 0.2px;
  }
  .brand {
    position: absolute; color: var(--ink);
  }
  .brand-name {
    font-weight: 500; letter-spacing: 7px; line-height: 1;
  }
  .brand-tagline { font-weight: 400; line-height: 1; }
  .wall-brand { left: 351px; top: 38px; }
  .wall-brand .brand-name { font-size: 36px; }
  .wall-brand .brand-tagline { font-size: 15.5px; margin-top: 8px; }

  .chef-photo {
    position: absolute; left: 32px; top: 196px;
    width: 282px; height: 256px;
    border-radius: 48% 48% 46% 46% / 44% 44% 56% 56%;
    background: radial-gradient(ellipse at 45% 40%, #f4f2f0 0%, #d9d6d3 45%, #8d8a88 80%, #5b5856 100%);
  }

  .wall-headline {
    position: absolute; left: 343px; top: 200px;
    font-weight: 700; font-size: 44px; line-height: 42px;
    color: var(--ink); letter-spacing: -0.5px;
  }
  .wall-body {
    position: absolute; left: 343px; top: 382px; width: 232px;
    font-size: 13.6px; line-height: 15.6px; color: var(--body-grey);
  }
  .web-address { color: var(--white); font-weight: 400; }
  .web-address strong { color: var(--lime); font-weight: 500; }
  .wall-web {
    position: absolute; left: 46px; top: 510px; font-size: 19px;
  }

  /* ---------- 2x2 counter ---------- */
  .counter {
    position: absolute;
    left: 752px; top: 510px;
    width: 348px; height: 263px;
    background: var(--ink);
    overflow: hidden;
    box-shadow: 0 4px 6px rgba(0,0,0,0.25);
  }
  .counter .counter-wave { position: absolute; inset: 0; }
  .counter-web {
    position: absolute; left: 0; right: 0; top: 31px;
    text-align: center; font-size: 10.5px;
  }
  .counter-brand {
    left: 0; right: 0; top: 80px; text-align: center; color: var(--white);
  }
  .counter-brand .brand-name { font-size: 29px; letter-spacing: 6px; }
  .counter-brand .brand-tagline { font-size: 12.5px; color: var(--lime); margin-top: 6px; }

  /* ---------- labels ---------- */
  .piece-label {
    position: absolute;
    font-family: "Open Sans", sans-serif; font-weight: 700;
    font-size: 31px; color: var(--ink); white-space: nowrap;
    transform: translateX(-50%);
  }
  .label-wall { left: 385px; top: 824px; }
  .label-counter { left: 931px; top: 812px; }
</style>
</head>
<body>

  <section class="back-wall" aria-label="3x3 booth back wall">
    <svg class="wall-shapes" viewBox="0 0 592 592" width="592" height="592" aria-hidden="true">
      <rect width="592" height="592" fill="var(--white)"/>
      <path d="M0 0 H592 V143 C560 165 520 182 475 182 C380 182 300 73 167 73 C95 73 40 110 0 140 Z" fill="var(--lime)"/>
      <path d="M110 82 C230 90 330 230 475 234 C530 236 565 220 592 203" fill="none" stroke="var(--lime)" stroke-width="0.8"/>
      <ellipse cx="475" cy="540" rx="140" ry="72" fill="var(--mist)"/>
      <path d="M0 437 C50 410 100 403 145 403 C290 403 360 521 480 521 C530 521 565 505 592 490 V592 H0 Z" fill="var(--ink)"/>
    </svg>

    <div class="wall-phone">+44 (0)2039461275</div>

    <div class="brand wall-brand">
      <div class="brand-name">VERDANO</div>
      <div class="brand-tagline">Food Hygiene &amp; Health Safety</div>
    </div>

    <div class="chef-photo" role="img" aria-label="Photo of a chef in whites plating a bowl of fresh fruit in a professional kitchen"></div>

    <h1 class="wall-headline">Our<br>Promise<br>is Peace<br>of Mind</h1>

    <p class="wall-body">Take advantage of our extensive knowledge, commitment to superior customer service, and dedication to excellence.</p>

    <div class="web-address wall-web">www.<strong>verdanosolutions</strong>.co.uk</div>
  </section>

  <section class="counter" aria-label="2x2 pop up counter">
    <svg class="counter-wave" viewBox="0 0 348 263" width="348" height="263" aria-hidden="true">
      <path d="M0 190 C25 178 45 170 66 170 C150 170 190 232 256 232 C295 232 325 212 348 196 V263 H0 Z" fill="var(--lime)"/>
    </svg>
    <div class="web-address counter-web">www.<strong>verdanosolutions</strong>.co.uk</div>
    <div class="brand counter-brand">
      <div class="brand-name">VERDANO</div>
      <div class="brand-tagline">Food Hygiene &amp; Health Safety</div>
    </div>
  </section>

  <div class="piece-label label-wall">3x3 booth scheel</div>
  <div class="piece-label label-counter">2x2 pop up Counter</div>

</body>
</html>
```